Pemberton Dialworks Business Card Design

Double Sided Business Card Design for a Locksmith company specializing in Safecracking, safe & vault service.

```html
<!DOCTYPE html>
<html lang="en">
<head>
<meta charset="utf-8">
<title>Pemberton Dialworks Business Card</title>
<link rel="stylesheet" href="https://fonts.googleapis.com/css2?family=Montserrat:wght@500;800&family=Roboto:wght@400;500&display=swap">
<style>
  :root {
    --bg: #e9e6e2;
    --card: #fbfbfa;
    --green: #2a7a34;
    --ink: #1b1b1b;
    --shadow: rgba(60, 45, 30, 0.18);
  }
  * { margin: 0; padding: 0; box-sizing: border-box; }
  html, body {
    width: 1200px;
    height: 800px;
    overflow: hidden;
    background: var(--bg);
  }
  .sheet {
    width: 1200px;
    height: 800px;
    display: flex;
    align-items: center;
    justify-content: center;
    gap: 40px;
  }
  .card {
    width: 540px;
    height: 309px;
    background: var(--card);
    box-shadow: 0 10px 30px var(--shadow);
    display: flex;
    flex-direction: column;
    align-items: center;
    justify-content: center;
    text-align: center;
  }

  /* Contact side */
  .person-name {
    font-family: "Montserrat", sans-serif;
    font-weight: 800;
    font-size: 26px;
    letter-spacing: 0.5px;
    color: var(--green);
    text-transform: uppercase;
    line-height: 1;
  }
  .person-role {
    font-family: "Roboto", sans-serif;
    font-size: 17px;
    color: var(--ink);
    margin-top: 4px;
  }
  .contact-icons {
    display: flex;
    gap: 14px;
    margin: 10px 0 10px;
  }
  .contact-icons svg { width: 16px; height: 16px; }
  .contact-lines {
    font-family: "Roboto", sans-serif;
    font-size: 15px;
    color: var(--ink);
    line-height: 1.55;
  }
  .address {
    font-family: "Roboto", sans-serif;
    font-size: 15px;
    color: var(--green);
    line-height: 1.4;
    margin-top: 16px;
  }

  /* Brand side */
  .brand {
    display: flex;
    align-items: center;
    gap: 18px;
  }
  .brand-mark {
    width: 74px;
    height: 74px;
    border-radius: 50%;
    background: var(--green);
    flex-shrink: 0;
  }
  .brand-text { text-align: left; }
  .brand-name {
    font-family: "Montserrat", sans-serif;
    font-weight: 800;
    font-size: 30px;
    line-height: 1.05;
    color: var(--green);
    text-transform: uppercase;
  }
  .brand-web {
    font-family: "Roboto", sans-serif;
    font-size: 14px;
    letter-spacing: 2px;
    color: var(--green);
    margin-top: 8px;
  }
</style>
</head>
<body>
<main class="sheet">
  <section class="card card-contact">
    <h1 class="person-name">Martin Hale</h1>
    <p class="person-role">Manager</p>
    <div class="contact-icons">
      <svg viewBox="0 0 16 16" aria-label="Phone" role="img">
        <circle cx="8" cy="8" r="7" fill="none" stroke="var(--green)" stroke-width="1.2"/>
        <path d="M5.3 4.6l1.3-.2.7 1.6-.8.7a5 5 0 0 0 2.3 2.3l.7-.8 1.6.7-.2 1.3c-3 .3-5.9-2.6-5.6-5.6z" fill="var(--green)"/>
      </svg>
      <svg viewBox="0 0 16 16" aria-label="Email" role="img">
        <circle cx="8" cy="8" r="7" fill="none" stroke="var(--green)" stroke-width="1.2"/>
        <rect x="4.2" y="5.3" width="7.6" height="5.4" rx="0.6" fill="var(--green)"/>
        <path d="M4.4 5.6L8 8.3l3.6-2.7" fill="none" stroke="var(--card)" stroke-width="0.8"/>
      </svg>
      <svg viewBox="0 0 16 16" aria-label="Website" role="img">
        <circle cx="8" cy="8" r="7" fill="none" stroke="var(--green)" stroke-width="1.2"/>
        <circle cx="8" cy="8" r="3.6" fill="none" stroke="var(--green)" stroke-width="1"/>
        <path d="M4.4 8h7.2M8 4.4c-1.6 2-1.6 5.2 0 7.2M8 4.4c1.6 2 1.6 5.2 0 7.2" fill="none" stroke="var(--green)" stroke-width="0.8"/>
      </svg>
    </div>
    <p class="contact-lines">
      555-010-0147<br>
      pembertondialworks@mailbox.com<br>
      pembertondialworks.com
    </p>
    <p class="address">
      480 Harlow Ridge Rd, Suite 210<br>
      Brookfield , TX , 75290
    </p>
  </section>

  <section class="card card-brand">
    <div class="brand">
      <div class="brand-mark"></div>
      <div class="brand-text">
        <p class="brand-name">Pemberton<br>Dialworks</p>
        <p class="brand-web">www.pembertondialworks.com</p>
      </div>
    </div>
  </section>
</main>
</body>
</html>
```